KESTRELMAR NAUTICA SUPPLIERS SELL SHEETS

Create a group of Sell Sheets that can be used in client meetings and willbe incorporated into web site pages in the future. We wish to highlight our Mission Statement / Company Bio / Services and Products offered. This piece may be 8 to 12 pages. In the near future this will grow to include an on-line Catalog with 300 to 500 pages of product offerings.

It will not list individual products and prices but rather will serve as a New Business introduction using brief descriptive text and a lot of industry photos. At this time we do have a Logo and Tag Line which will be used.

The image we need to portray is High End Quality Sales, Service, Professional Industry Experience and Reliability. My personal experience includes 27 years as a ship´s Captain working all over the world.

We are a start-up Ship´s Chandler service, located in Macae, Brasil. We will sell products and inspection services to the Offshore Petroleum Industry which includes vessels and platforms. These products will include the simple monthly supply replenishment (like paper towels / laundry soap / drinking water) to the more technical, like Pop Off Valves (sales & inspection certifications), Transfer Hoses, Sales Service and Certifications, OEM Filters for Engines& Generators, Anchor Harware, Nautical Bulbs & Light Fixtures Safety Gear and hundreds of other items.

We will have a group of EMERGENCY GEAR on-hand in our warehouse, to supply in cases like a lost anchor for example. We willoffer a Guaranteed 30 hour delivery anywhere in Brasil. These vessels work at a rate of up to $50K per day and cannot afford what is called`Down Time` or time off the clock.

All text will be supplied in both English and Portuguese. I prefer that each block of text will show both languages with a distinctive color or typeface for each. Please present your ideas on how to deal with the two languages.

Sorry for any mis-spellings but today I am forced to work on a Portuguese keyboard.

Target Market(s)

Ship´s Captains, Purchasing Managers, Company Directors, Engineers

Industry/Entity Type

Business

Requirements
Must have
• I am open to a Professional, High End look. I would like to incorporate photos and ``historical`` illustrations to tella story, which I will supply.

I have attached our new Company Logo which has the tag line....``TO STAY THE COURSE´´. We would like to repeat the logo and tag line whenever possible without being too obnoxious.

```html
<!DOCTYPE html>
<html lang="en">
<head>
<meta charset="utf-8">
<title>Kestrelmar Nautica Suppliers – Sell Sheet Inner Side</title>
<link rel="stylesheet" href="https://fonts.googleapis.com/css2?family=Crimson+Pro:wght@400&family=Open+Sans:wght@400;700&display=swap">
<style>
  :root {
    --page-bg: #ece7df;
    --sheet: #ffffff;
    --ink: #1a1a1a;
    --gold: #f5c21a;
    --gold-light: #fbe08a;
    --green: #24512a;
    --green-mid: #6c8a2a;
    --bullet: #1f8a2a;
    --rule: #333333;
  }
  * { box-sizing: border-box; margin: 0; padding: 0; }
  html, body { width: 1200px; height: 960px; overflow: hidden; background: var(--page-bg); }
  .sheet {
    position: absolute; left: 62px; top: 45px; width: 1096px; height: 845px;
    background: var(--sheet); overflow: hidden;
    box-shadow: 0 2px 6px rgba(0,0,0,.25);
  }
  .decor { position: absolute; inset: 0; width: 1096px; height: 845px; }
  .lang-title {
    position: absolute; top: 12px; font-family: "Open Sans", sans-serif; font-weight: 700;
    font-size: 31px; color: var(--ink); letter-spacing: -0.5px;
  }
  .lang-title.en { left: 6px; }
  .lang-title.pt { right: 6px; }
  .pill {
    position: absolute; width: 224px; height: 33px; border-radius: 50%;
    background: radial-gradient(ellipse at 50% 40%, var(--gold-light), var(--gold) 75%);
    font-family: "Open Sans", sans-serif; font-weight: 700; font-size: 23px;
    color: var(--ink); text-align: center; line-height: 33px; letter-spacing: -0.3px;
  }
  .body-copy {
    position: absolute; font-family: "Crimson Pro", serif; color: var(--ink);
    white-space: nowrap; transform-origin: 0 0; transform: scaleX(0.64);
  }
  .body-copy.en { left: 24px; top: 127px; font-size: 17.5px; line-height: 27px; }
  .body-copy.en p + p { margin-top: 27px; }
  .body-copy.pt { left: 745px; top: 124px; font-size: 17px; line-height: 24.7px; }
  .body-copy.pt p + p { margin-top: 18px; }
  .service-list { position: absolute; list-style: none; font-family: "Open Sans", sans-serif; color: var(--ink); }
  .service-list li { position: relative; padding-left: 22px; }
  .service-list li::before {
    content: ""; position: absolute; left: 0; width: 12px; height: 15px; border-radius: 50%;
    background: var(--bullet);
  }
  .service-list.en { left: 16px; top: 603px; width: 350px; font-weight: 700; font-size: 16.4px; line-height: 27px; }
  .service-list.en li { margin-bottom: 2px; }
  .service-list.en li::before { top: 7px; }
  .service-list.pt { left: 746px; top: 596px; width: 330px; font-size: 14px; line-height: 20px; }
  .service-list.pt li { margin-bottom: 7px; }
  .service-list.pt li::before { top: 4px; }
  .photo { position: absolute; }
  .photo.plant { left: 370px; top: 63px; width: 182px; height: 120px; background: linear-gradient(160deg, #c9d4dc, #7f8e9a 55%, #3a4a66); }
  .photo.workshop { left: 546px; top: 202px; width: 174px; height: 115px; background: linear-gradient(170deg, #b8b8b4, #d49a3c 45%, #6b7078); }
  .photo.yacht { left: 366px; top: 322px; width: 180px; height: 120px; background: linear-gradient(180deg, #7f9fbf, #e8ecef 55%, #6d7070); }
  .photo.gears { left: 544px; top: 475px; width: 184px; height: 142px; background: linear-gradient(135deg, #2b2b2b, #a9a9a9 45%, #ececec 60%, #444); }
  .photo.rig { left: 370px; top: 631px; width: 266px; height: 159px; background: linear-gradient(180deg, #bcd4e6, #8fb0c8 50%, #3d6a86); }
</style>
</head>
<body>
<main class="sheet">
  <svg class="decor" viewBox="0 0 1096 845" aria-hidden="true">
    <defs>
      <linearGradient id="swoosh-left" x1="0" x2="1" y1="0" y2="0">
        <stop offset="0" stop-color="#f5c21a"/><stop offset="0.45" stop-color="#c9a81c"/><stop offset="1" stop-color="#24512a"/>
      </linearGradient>
      <linearGradient id="swoosh-right" x1="0" x2="1" y1="0" y2="0">
        <stop offset="0" stop-color="#24512a"/><stop offset="0.55" stop-color="#c9a81c"/><stop offset="1" stop-color="#f5c21a"/>
      </linearGradient>
      <linearGradient id="footer-band" x1="0" x2="1" y1="0" y2="0">
        <stop offset="0" stop-color="#f5c21a"/><stop offset="0.4" stop-color="#d9b31e"/><stop offset="0.7" stop-color="#6c8a2a"/><stop offset="1" stop-color="#24512a"/>
      </linearGradient>
    </defs>
    <path d="M0 0 H366 V6 C250 14 95 42 0 96 Z" fill="url(#swoosh-left)"/>
    <path d="M728 0 H1096 V80 C1010 42 860 12 728 6 Z" fill="url(#swoosh-right)"/>
    <path d="M728 805 C880 800 1000 770 1096 715 V845 H728 Z" fill="#24512a"/>
    <path d="M0 812 C300 790 700 835 1096 795 V845 H0 Z" fill="url(#footer-band)"/>
    <line x1="366" y1="0" x2="366" y2="818" stroke="#333" stroke-width="1.5"/>
    <line x1="728" y1="0" x2="728" y2="810" stroke="#333" stroke-width="1.5"/>
  </svg>

  <h2 class="lang-title en">ENGLISH</h2>
  <h2 class="lang-title pt">PORTUGUESE</h2>

  <section class="panel-en">
    <h3 class="pill" style="left:10px;top:85px;">INTRODUCTION</h3>
    <div class="body-copy en">
      <p>We are a start-up Ship´s Chandler service, located in Macae, Brasil. We<br>will sell products and inspection services to the Offshore Petroleum<br>Industry which includes vessels and platforms. These products will<br>include the simple monthly supply replenishment (like paper towels /<br>laundry soap / drinking water) to the more technical, like Pop Off Valves<br>(sales &amp; inspection certifications), Transfer Hoses, Sales Service and<br>Certifications, OEM Filters for Engines&amp; Generators, Anchor Harware,<br>Nautical Bulbs &amp; Light Fixtures Safety Gear and hundreds of other<br>items.</p>
      <p>We will have a group of EMERGENCY GEAR on-hand in our<br>warehouse, to supply in cases like a lost anchor for example. We<br>willoffer a Guaranteed 30 hour delivery anywhere in Brasil. These<br>vessels work at a rate of up to $50K per day and cannot afford what is<br>called`Down Time` or time off the clock.</p>
    </div>
    <h3 class="pill" style="left:10px;top:558px;">SERVICES</h3>
    <ul class="service-list en">
      <li>Services to the Offshore Petroleum Industry which includes vessels.</li>
      <li>Transfer Hoses, Sales Service and Certifications.</li>
      <li>EMERGENCY GEAR group.</li>
      <li>OEM Filters for Engines&amp; Generators, Anchor Harware, Nautical Bulbs.</li>
    </ul>
  </section>

  <section class="panel-photos">
    <div class="photo plant" role="img" aria-label="Photo of engineers working among industrial piping"></div>
    <div class="photo workshop" role="img" aria-label="Photo of a large industrial workshop with overhead crane"></div>
    <div class="photo yacht" role="img" aria-label="Photo of a large white vessel at sea"></div>
    <div class="photo gears" role="img" aria-label="Photo of close-up steel gears"></div>
    <div class="photo rig" role="img" aria-label="Photo of an offshore oil platform on the water"></div>
  </section>

  <section class="panel-pt" lang="pt">
    <h3 class="pill" style="left:746px;top:83px;">INTRODUÇÃO</h3>
    <div class="body-copy pt">
      <p>Somos um navio de arranque do serviço de Chandler, localizada em<br>Macaé, Brasil. Vamos vender produtos e serviços de inspeção para a<br>Indústria de Petróleo Offshore, que inclui navios e plataformas. Estes<br>produtos incluem o reabastecimento mensal simples (como toalhas de<br>papel / água sabão em pó / bebidas) para o mais técnico, como Pop Off<br>Válvulas (vendas e certificações de inspecção), mangueiras de<br>transferência, vendas, serviços e certificações, Filtros de OEM para<br>Motores e Geradores, âncora Harware, lâmpadas náuticas e<br>equipamentos de segurança luminárias e centenas de outros itens.</p>
      <p>Nós temos um grupo de equipamentos de emergência na mão em nosso<br>armazém, para suprir, em casos como uma âncora perdida por exemplo.<br>Nós willoffer uma entrega garantida 30 horas em qualquer lugar no<br>Brasil. Estas embarcações trabalhar em uma taxa de até R $ 50 mil por<br>dia e não pode pagar o que é chamado `Down Time 'ou tempo fora do<br>relógio.</p>
    </div>
    <h3 class="pill" style="left:746px;top:547px;">SERVIÇOS</h3>
    <ul class="service-list pt">
      <li>Serviços para o Petróleo Offshore<br>Indústria, que inclui vasos.</li>
      <li>Mangueiras de transferência, o serviço de<br>vendas Certificações.</li>
      <li>Grupo de equipamentos de emergência.</li>
      <li>Filtros de OEM para Motores e Geradores,<br>Hardware âncora, lâmpadas náuticas.</li>
    </ul>
  </section>
</main>
</body>
</html>
```